International Medical Company Needs a Website Design for a Support Site

We need a website design for a support site we are doing for ostomates called Bright Rebounds. We are an international company but this website is for our Australian market.

The website is a support site for people who are living with an Ostomy or Bowel Disease. This is a site where they can read other ostomates' stories and how they are dealing with the fact that they have to wear a pouch everyday.

The URL for our US site is: http://www.brightrebounds-example.com/

We need to use the same logo but we have freedom around the color scheme. We are not fond of the brown color scheme used in our US site and are happy for designs to be submitted with alternatives.

• We want the design to be clean, inspiring, modern and inviting.
• We would like to see a design for the mainpage / homepage and one of the subpages
• We only require the PSD / image files (no HTML needed)

Attached to this project is our sitemap, an example wireframe and the logos. We are happy for you to play around with different options and don't have to stick to the layout shown in the wireframe.

If you have any further questions please ask.

```html
<!DOCTYPE html>
<html lang="en">
<head>
<meta charset="utf-8">
<title>Bright Rebounds</title>
<link href="https://fonts.googleapis.com/css2?family=PT+Sans:wght@400;700&display=swap" rel="stylesheet">
<style>
:root{
  --teal:#6fa39a;
  --teal-line:#9cc4bd;
  --orange:#c46d1e;
  --ink:#3a3a3a;
  --text:#444;
  --muted:#777;
  --rule:#8c9bb0;
  --panel:#efefef;
  --stripe:#e6e6e6;
  --footer:#3c3c3c;
  --banner:#6a6a6a;
  --white:#fff;
}
*{margin:0;padding:0;box-sizing:border-box}
html,body{width:931px;height:1200px;overflow:hidden;background:var(--white)}
body{position:relative;font-family:"PT Sans",Arial,sans-serif;color:var(--text)}
.abs{position:absolute}
a{color:inherit;text-decoration:none}

/* header */
.brand{left:124px;top:86px;font-size:13px;letter-spacing:1.5px;color:var(--ink);display:flex;align-items:center;gap:6px}
.brand .dot{width:9px;height:9px;background:var(--orange)}
.country{left:504px;top:12px;font-size:12px;color:var(--ink)}
.country:after{content:"";display:inline-block;margin-left:5px;border:4px solid transparent;border-top-color:#bbb;vertical-align:-1px}
.sep{left:569px;top:8px;width:1px;height:24px;background:#ccc}
.search{left:582px;top:5px;width:224px;height:28px;background:#eee;font-size:13px;color:var(--ink);padding:6px 10px}
.search svg{position:absolute;right:8px;top:5px}
.btn-share-small{left:699px;top:48px;width:108px;height:30px;background:var(--teal);color:var(--white);font-size:13px;display:flex;align-items:center;justify-content:center;gap:7px}
.nav{right:125px;top:89px;display:flex;gap:19px;font-size:14px;color:var(--ink)}
.nav .active{color:var(--orange)}
.header-rule{left:0;top:113px;width:931px;height:2px;background:var(--orange)}

/* hero */
.hero{left:0;top:115px;width:931px;height:307px;background:linear-gradient(180deg,#a3c4bd 0%,#d2dcc4 45%,#ecdcb6 75%,#ebbfa5 100%)}
.hero-hands{left:390px;top:115px;width:420px;height:200px;background:radial-gradient(ellipse at 50% 55%,#d99a7c 0%,#e2ae90 40%,rgba(226,174,144,0) 72%)}
.hero-rule{left:0;top:421px;width:931px;height:2px;background:var(--teal-line)}
.hero-title{left:125px;top:192px;font-size:18px;color:#555}
.hero-text{left:125px;top:235px;width:300px;font-size:12px;line-height:15px;color:#555}
.btn-hero{left:124px;top:304px;width:148px;height:40px;background:#555;color:var(--white);font-size:17px;display:flex;align-items:center;justify-content:center;border-radius:2px}
.hero-sep{left:287px;top:312px;width:1px;height:26px;background:#f4f0e0}
.read-others{left:300px;top:311px;font-size:17px;color:#4f7f8a;border-bottom:1px dotted #4f7f8a;line-height:20px}

/* about */
.section-title{font-size:17px;color:var(--ink)}
.about-title{left:126px;top:448px}
.about-rule{left:125px;top:472px;width:432px;height:1px;background:var(--rule)}
.about-copy{left:124px;top:484px;width:432px;font-size:7.6px;line-height:9.2px;color:#333}
.about-copy p{margin-bottom:9.3px}
.learn{font-size:9px;color:#333;display:flex;align-items:center;gap:5px}
.learn svg{flex:none}
.about-learn{left:123px;top:634px}

/* news */
.news-title{left:571px;top:448px}
.news-panel{left:571px;top:469px;width:236px;height:230px;background:repeating-linear-gradient(135deg,var(--panel) 0 3px,var(--stripe) 3px 4px);padding:14px 13px 0 13px}
.news-item{font-size:8.3px;line-height:10.8px;color:#333;margin-bottom:5px}
.news-item h3{font-size:8.6px;font-weight:700;line-height:11px;color:#222}
.news-item .date{color:var(--orange);font-size:7.5px;line-height:9px}
.news-item .learn{justify-content:flex-end;margin-top:4px;margin-right:3px}

/* featured */
.featured-title{left:124px;top:718px}
.featured-rule{left:124px;top:739px;width:683px;height:1px;background:var(--teal-line)}
.card{top:770px;width:213px;height:192px;background:repeating-linear-gradient(135deg,var(--panel) 0 3px,var(--stripe) 3px 4px)}
.card-1{left:125px}
.card-2{left:360px}
.card-3{left:594px}
.card h2{position:absolute;left:8px;top:5px;font-size:17px;font-weight:400;color:var(--ink)}
.card .card-rule{position:absolute;left:9px;top:30px;width:187px;height:1px;background:var(--rule)}
.card .photo{position:absolute;left:0;top:41px;width:213px;height:102px}
.photo-hands{background:linear-gradient(100deg,#33619a 0%,#6d8fb8 35%,#e8c6b2 60%,#c99f8a 80%,#5a7fb0 100%)}
.photo-palm{background:radial-gradient(ellipse at 45% 50%,#d9a184 0%,#e9c3a8 35%,#f5e8dc 70%,#faf4ec 100%)}
.card .btn-learn{position:absolute;left:7px;top:157px;width:90px;height:21px;background:var(--white);border:1px solid #ddd;font-size:9px;color:#333;display:flex;align-items:center;justify-content:center}
.card-3 h2{left:15px;top:10px}
.card-3 .card-rule{left:15px;top:35px;width:183px}
.card-3 p{position:absolute;left:15px;top:58px;width:185px;font-size:7.8px;line-height:9.3px;color:#333}
.card-3 .btn-share{position:absolute;left:13px;top:137px;width:110px;height:30px;background:var(--teal);color:var(--white);font-size:13px;display:flex;align-items:center;justify-content:center;gap:7px}

/* footer */
.footer{left:0;top:999px;width:931px;height:201px;background:var(--footer);border-top:2px solid var(--teal-line)}
.foot-title{font-size:12px;color:#eee}
.testi-title{left:126px;top:1022px}
.testi-text{left:126px;top:1046px;width:290px;font-size:10px;line-height:11.3px;color:#b8b8b8}
.testi-name{left:355px;top:1103px;font-size:10px;font-weight:700;font-style:italic;color:#eee}
.banners-title{left:469px;top:1022px}
.banner{top:1048px;width:70px;height:64px;background:var(--banner)}
.b1{left:469px}.b2{left:554px}.b3{left:644px}.b4{left:734px}
.foot-links{left:0;width:931px;top:1165px;display:flex;justify-content:center;gap:9px;font-size:12px;font-weight:700;color:#eee;padding-right:12px}
</style>
</head>
<body>

<header>
  <div class="abs brand"><span>BRIGHTREBOUNDS</span><span class="dot"></span></div>
  <div class="abs country">Country</div>
  <div class="abs sep"></div>
  <div class="abs search">Search
    <svg width="20" height="20" viewBox="0 0 20 20" fill="none" stroke="#fff" stroke-width="1.6"><circle cx="8" cy="8" r="6"/><path d="M12.5 12.5l6 6"/></svg>
  </div>
  <a class="abs btn-share-small" href="#">Share a story
    <svg width="15" height="15" viewBox="0 0 15 15" fill="none" stroke="#fff" stroke-width="1.3"><circle cx="7.5" cy="7.5" r="6.5"/><path d="M7.5 4v7M4 7.5h7"/></svg>
  </a>
  <nav class="abs nav">
    <a class="active" href="#">About Us</a><a href="#">Personal</a><a href="#">Stories</a><a href="#">Tips for Living</a><a href="#">News</a><a href="#">Resources</a><a href="#">Contact Us</a>
  </nav>
  <div class="abs header-rule"></div>
</header>

<section>
  <div class="abs hero" role="img" aria-label="Soft sky-to-sunset photograph background"></div>
  <div class="abs hero-hands" role="img" aria-label="Photograph of two people holding hands"></div>
  <div class="abs hero-rule"></div>
  <h1 class="abs hero-title" style="font-weight:400">Sharing stories &amp; Giving Hope</h1>
  <p class="abs hero-text">to people around the world who are facing inflammatory bowel disease, colorectal cancer or have had ostomy surgery</p>
  <a class="abs btn-hero" href="#">Share a story</a>
  <div class="abs hero-sep"></div>
  <a class="abs read-others" href="#">or Read others</a>
</section>

<section>
  <h2 class="abs section-title about-title" style="font-weight:400">What is Bright Rebounds</h2>
  <div class="abs about-rule"></div>
  <div class="abs about-copy">
    <p>Lorem Ipsum has been the industry's standard dummy text ever since the 1500s, when an unknown printer took a galley of type and scrambled it to make a type specimen book. It has survived not only five centuries, but also the leap into electronic typesetting, remaining essentially unchanged.</p>
    <p>Lorem Ipsum has been the industry's standard dummy text ever since the 1500s, when an unknown printer took a galley of type and scrambled it to make a type specimen book. It has survived not only five centuries, but also the leap into electronic typesetting, remaining essentially unchanged.</p>
    <p>Lorem Ipsum has been the industry's standard dummy text ever since the 1500s, when an unknown printer took a galley of type and scrambled it to make a type specimen book. It has survived not only five centuries, but also the leap into electronic typesetting, remaining essentially unchanged.</p>
    <p>Lorem Ipsum has been the industry's standard dummy text ever since the 1500s, when an unknown printer took a galley of type and scrambled it to make a type specimen book. It has survived not only five centuries, but also the leap into electronic typesetting, remaining essentially unchanged.</p>
  </div>
  <a class="abs learn about-learn" href="#">Learn More
    <svg width="10" height="8" viewBox="0 0 10 8" fill="none" stroke="#7fb5ad" stroke-width="1.5"><path d="M1 1l3 3-3 3M5 1l3 3-3 3"/></svg>
  </a>
</section>

<section>
  <h2 class="abs section-title news-title" style="font-weight:400">Latest News</h2>
  <div class="abs news-panel">
    <div class="news-item">
      <h3>Bright Rebounds® Recognizes Former Principal, Gordon Ashby, As National Award Recipient</h3>
      <div class="date">August 21, 2013</div>
      <div>Lifelong educator pays it forward by teaching others how to succeed after ostomy surgery</div>
      <a class="learn" href="#">Learn More <svg width="10" height="8" viewBox="0 0 10 8" fill="none" stroke="#7fb5ad" stroke-width="1.5"><path d="M1 1l3 3-3 3M5 1l3 3-3 3"/></svg></a>
    </div>
    <div class="news-item">
      <h3>Congratulations to Gordon Ashby of Riverton,</h3>
      <div class="date">August 21, 2013</div>
      <div>MD, named this year's Bright Rebounds® National Award recipient at at the Continence Care Nurses Guild (CCNG) 45th Annual ...</div>
      <a class="learn" href="#">Learn More <svg width="10" height="8" viewBox="0 0 10 8" fill="none" stroke="#7fb5ad" stroke-width="1.5"><path d="M1 1l3 3-3 3M5 1l3 3-3 3"/></svg></a>
    </div>
    <div class="news-item">
      <h3>A Message from Peter Lindqvist</h3>
      <div class="date">May 22, 2013</div>
      <div>It is hard to believe that Bright Rebounds is almost 30 years old now but it is! Looking back it was the ...</div>
    </div>
  </div>
</section>

<section>
  <h2 class="abs section-title featured-title" style="font-weight:400">Featured Stories</h2>
  <div class="abs featured-rule"></div>

  <article class="abs card card-1">
    <h2>Lena Morales</h2>
    <div class="card-rule"></div>
    <div class="photo photo-hands" role="img" aria-label="Photograph of clasped hands resting on a lap"></div>
    <a class="btn-learn" href="#">Learn More</a>
  </article>

  <article class="abs card card-2">
    <h2>Dana Whitfield</h2>
    <div class="card-rule"></div>
    <div class="photo photo-palm" role="img" aria-label="Photograph of an open outstretched hand"></div>
    <a class="btn-learn" href="#">Learn More</a>
  </article>

  <article class="abs card card-3">
    <h2>Share your own story</h2>
    <div class="card-rule"></div>
    <p>Lorem Ipsum has been the industry's standard dummy text ever since the 1500s, when an unknown printer took a galley of type and scrambled it to make a type specimen book. It has survived not only five centuries, but also the leap into electronic typesetting, remaining essentially unchanged.</p>
    <a class="btn-share" href="#">Share a story
      <svg width="15" height="15" viewBox="0 0 15 15" fill="none" stroke="#fff" stroke-width="1.3"><circle cx="7.5" cy="7.5" r="6.5"/><path d="M7.5 4v7M4 7.5h7"/></svg>
    </a>
  </article>
</section>

<footer>
  <div class="abs footer"></div>
  <h3 class="abs foot-title testi-title" style="font-weight:400">Testimonials</h3>
  <p class="abs testi-text">Lorem Ipsum is simply dummy text of the printing and typesetting industry. Lorem Ipsum has been the industry's standard dummy text ever since the 1500s, when an unknown printer took a galley of type and scrambled</p>
  <div class="abs testi-name">Clara D.</div>
  <h3 class="abs foot-title banners-title" style="font-weight:400">Banners</h3>
  <div class="abs banner b1"></div>
  <div class="abs banner b2"></div>
  <div class="abs banner b3"></div>
  <div class="abs banner b4"></div>
  <nav class="abs foot-links">
    <a href="#">Legal notice</a><a href="#">Privacy Policy</a><a href="#">Sitemap</a><a href="#">Contact</a><a href="#">FAQ's</a>
  </nav>
</footer>

</body>
</html>
```